Flyer für Unterstützung in der Personalarbeit
Zielgruppe
HR Freelancer, bitte Dienstleistung für Unternehmen an, die temporär Unterstützung in der Personalarbeit (Personalprozesse, Recruiting, Lohn- und Gehaltsabrechnung, HR Management, Administration) benötigen.
Aufgabenstellung
Ich benötige einen mehrseitigen Flyer, der mich und meine Arbeit kurz vorstellt. Außerdem soll es in einem Teil darum gehen, warum ein HR Freelancer eine gute Wahl ist. Der Flyer/die Broschüre soll an Unternehmen versendet werden.
Ich wünsche mir ein modernes minimalistisches und dennoch ansprechendes Design. Ich benötige die Datei am Ende auch im Word Format, da ich zukünftig Referenzen und weitere Auftraggeber ergänzen muss.
Ich füge zudem verschiedene Bilder bei, dabei müssen nicht alle berücksichtigt werden.

```html
<!DOCTYPE html>
<html lang="de">
<head>
<meta charset="utf-8">
<title>HR Freelancer Flyer – Lena Marwitz</title>
<link href="https://fonts.googleapis.com/css2?family=Rubik:wght@400;500;700&family=Quicksand:wght@300;400;500&display=swap" rel="stylesheet">
<style>
  :root {
    --coral: #ea5545;
    --ink: #1e1e1e;
    --grey: #3c3c3c;
    --paper: #ffffff;
  }
  * { margin: 0; padding: 0; box-sizing: border-box; }
  html, body { width: 1200px; height: 402px; overflow: hidden; background: var(--paper); }
  body { font-family: "Rubik", Arial, sans-serif; color: var(--ink); position: relative; }

  .panel { position: absolute; }

  /* Left panel: reasons */
  .portrait-left {
    left: 0; top: 0; width: 185px; height: 393px;
    background: linear-gradient(90deg, #d9d6d2 0%, #e8e4e0 30%, #2a2a2d 55%, #1c1c1f 100%);
  }
  .reasons { left: 144px; top: 0; width: 251px; height: 393px; }
  .reasons-title {
    position: absolute; left: 0; top: 16px;
    color: var(--coral); font-weight: 700; font-size: 14.5px; white-space: nowrap;
  }
  .reason { position: absolute; left: 0; width: 251px; height: 48px; background: var(--paper); }
  .reason-head {
    background: var(--coral); color: #fff; font-weight: 500;
    font-size: 9.4px; height: 14.5px; line-height: 14.5px; padding-left: 6px;
  }
  .reason-text { font-size: 6.6px; line-height: 9px; padding: 4px 6px 0 6px; color: var(--ink); }

  /* Cover */
  .cover {
    left: 395px; top: 0; width: 405px; height: 213px; background: var(--coral);
    display: flex; flex-direction: column; align-items: center; justify-content: center; color: #fff;
  }
  .brand-name { font-family: "Quicksand", sans-serif; font-weight: 300; font-size: 33px; letter-spacing: 0.5px; line-height: 1; }
  .brand-role { font-family: "Quicksand", sans-serif; font-weight: 500; font-size: 13.5px; margin-top: 18px; letter-spacing: 0.4px; }

  .portrait-right {
    left: 800px; top: 0; width: 400px; height: 208px;
    background: linear-gradient(90deg, #d7dad8 0%, #c9ccc8 40%, #8a7f6c 60%, #b9bcba 80%, #9ea5a7 100%);
  }
  .divider-red { left: 800px; top: 208px; width: 400px; height: 5px; background: var(--coral); }

  /* Bottom middle */
  .cta { left: 415px; top: 258px; width: 200px; }
  .cta-head { color: var(--coral); font-weight: 700; font-size: 15.6px; line-height: 17px; }
  .cta-text { margin-top: 20px; font-size: 8.1px; line-height: 11px; }

  .contact { left: 659px; top: 258px; width: 200px; font-size: 8.1px; }
  .contact-name { color: var(--coral); font-weight: 700; font-size: 10.8px; }
  .contact-sub { line-height: 11px; margin-top: 2px; }
  .contact-list { list-style: none; margin-top: 11px; }
  .contact-list li { display: flex; align-items: center; height: 10.8px; }
  .contact-list li.gap { margin-top: 5px; }
  .contact-list svg { width: 7px; height: 7px; margin-right: 7px; flex: none; }

  .back-brand {
    left: 880px; top: 243px; width: 223px; text-align: center;
    color: var(--grey);
  }
  .back-brand .brand-name { font-size: 28px; }
  .back-brand .brand-role { font-size: 12.5px; margin-top: 14px; color: var(--ink); }

  .footer-band { left: 0; top: 393px; width: 1200px; height: 9px; background: var(--coral); }
</style>
</head>
<body>

  <div class="panel portrait-left" role="img" aria-label="Porträtfoto der HR-Freelancerin in schwarzem Blazer"></div>

  <section class="panel reasons">
    <h2 class="reasons-title">Warum ein HR-Freelancer?</h2>
    <div class="reason" style="top:55px"><div class="reason-head">1. Flexibilität</div><p class="reason-text">Freelancer können stundenweise oder projektbezogen engagiert werden – man bezahlt nur für tatsächlich benötigte Leistungen.</p></div>
    <div class="reason" style="top:103px"><div class="reason-head">2. Spezialisierte Expertise</div><p class="reason-text">Sie bringen Fachwissen aus verschiedenen Branchen mit und bieten sofortige Lösungen für spezifische HR-Aufgaben.</p></div>
    <div class="reason" style="top:151px"><div class="reason-head">3. Kosteneffizienz</div><p class="reason-text">Rekrutierung der passenden Talente für Ihr Unternehmen, inklusive vollständigem Bewerbermanagement und Vorstellungsgesprächen.</p></div>
    <div class="reason" style="top:199px"><div class="reason-head">4. Unabhängige Perspektive</div><p class="reason-text">Externe Freelancer bringen frische Ideen und können Prozesse objektiv bewerten und optimieren.</p></div>
    <div class="reason" style="top:247px"><div class="reason-head">5. Schnelle Verfügbarkeit</div><p class="reason-text">Freelancer sind sofort einsatzbereit und unterstützen kurzfristig bei Engpässen oder Projekten.</p></div>
    <div class="reason" style="top:295px"><div class="reason-head">6. Projektbezogene Unterstützung</div><p class="reason-text">Sie übernehmen zeitlich begrenzte Aufgaben und Projekte, von der Planung bis zur Umsetzung.</p></div>
    <div class="reason" style="top:343px"><div class="reason-head">7. Netzwerk und Erfahrung</div><p class="reason-text">Durch Erfahrung in verschiedenen Unternehmen bieten sie wertvolle Kontakte und Best Practices.</p></div>
  </section>

  <section class="panel cover">
    <div class="brand-name">lena marwitz</div>
    <div class="brand-role">HR Freelancer</div>
  </section>

  <div class="panel portrait-right" role="img" aria-label="Foto der HR-Freelancerin am Flussufer vor moderner Stadtarchitektur"></div>
  <div class="panel divider-red"></div>

  <section class="panel cta">
    <h2 class="cta-head">Lassen Sie uns Ihre HR-Themen gemeinsam erfolgreich gestalten!</h2>
    <p class="cta-text">Kontaktieren Sie mich gerne für ein unverbindliches Gespräch – ich freue mich darauf, Ihre HR-Prozesse zu optimieren und Ihr Team erfolgreich zu unterstützen.</p>
  </section>

  <section class="panel contact">
    <div class="contact-name">Lena Marwitz</div>
    <p class="contact-sub">Ihre HR-Freelancerin für<br>maßgeschneiderte Lösungen</p>
    <ul class="contact-list">
      <li><svg viewBox="0 0 10 10"><path d="M5 .8a3.2 3.2 0 0 0-3.2 3.2C1.8 6.4 5 9.4 5 9.4S8.2 6.4 8.2 4A3.2 3.2 0 0 0 5 .8z" fill="none" stroke="#ea5545" stroke-width="1.2"/><circle cx="5" cy="4" r="1.1" fill="#ea5545"/></svg>Waldhagen, Berlin</li>
      <li class="gap"><svg viewBox="0 0 10 10"><path d="M2.2 1h2l1 2.3-1.3.9a5.5 5.5 0 0 0 2 2l.9-1.3L9 6v2a1 1 0 0 1-1 1A7 7 0 0 1 1 2a1 1 0 0 1 1.2-1z" fill="#ea5545"/></svg>0176 / 55 01 84 27</li>
      <li><svg viewBox="0 0 10 10"><rect x=".8" y="2" width="8.4" height="6" fill="#ea5545"/><path d="M.8 2 5 5.3 9.2 2" fill="none" stroke="#fff" stroke-width=".8"/></svg>mail@lenamarwitz.de</li>
      <li><svg viewBox="0 0 10 10"><circle cx="5" cy="5" r="4.2" fill="#ea5545"/></svg>www.lenamarwitz.de</li>
      <li class="gap"><svg viewBox="0 0 10 10"><rect x="1" y="1" width="8" height="8" rx="1" fill="#ea5545"/></svg>&nbsp;Lena Marwitz</li>
    </ul>
  </section>

  <section class="panel back-brand">
    <div class="brand-name">lena marwitz</div>
    <div class="brand-role">HR Freelancer</div>
  </section>

  <div class="panel footer-band"></div>

</body>
</html>
```